Business Card Design

I want to pull elements/colors from Website. Attached is a screen shot. Do not want any buildings/building graphics/construction clichés. This is for a construction management firm but I want to keep it broad enough that I can expand into other areas. I do not want the logo to be limited. Thank you.
Updates

Please review the screen shot of the website. Please use the font and color of Brackwell Holdings, LLC on the website. Please use the tag line "Construction Management in the Palm Beaches" Please show contractor license ... CGC 7390462 You may use the back for the contact information. Please no phone/house icons. It does not have to be a black card. Thank you.

Target Market(s)

Professional people with money. Owners, Architects, Engineers, Developers, Real Estate Agents etc.

Industry/Entity Type

Construction

Contact Information for Business Card

Brackwell Holdings, LLC
Construction Management

Dean T Brackwell
418 Ostrander Court #73
North Palm Beach, FL 33412
(561) 555-0187
www.BrackwellHoldings.example

Requirements
Must have
• Clean, crisp, modern.

Broad enough that it is not trapped into a particular industry.

My goal is to expand into different markets, different industries.

Should not have
• The back of the card should not be colored in any way. Rubs off on other cards.

Do not want any buildings/building graphics/construction clichés.

```html
<!DOCTYPE html>
<html lang="en">
<head>
<meta charset="utf-8">
<title>Brackwell Holdings – Business Card</title>
<link rel="stylesheet" href="https://fonts.googleapis.com/css2?family=Roboto+Condensed:wght@700&family=Open+Sans:wght@300;400;700&display=swap">
<style>
  :root {
    --stage: #1c1c1c;
    --card-black: #0e0e0e;
    --card-black-soft: #2a2a2a;
    --band-grey: #4b4b4b;
    --text-white: #f4f4f4;
    --text-light: #cfcfcf;
    --text-band: #dcdcdc;
  }
  * { box-sizing: border-box; margin: 0; padding: 0; }
  html, body {
    width: 1200px;
    height: 1000px;
    overflow: hidden;
    background: var(--stage);
  }
  .canvas {
    width: 1200px;
    height: 1000px;
    display: flex;
    align-items: center;
    justify-content: center;
  }
  .business-card {
    width: 840px;
    height: 480px;
    position: relative;
    overflow: hidden;
    box-shadow: 0 18px 50px rgba(0,0,0,0.55);
    font-family: "Open Sans", Arial, sans-serif;
  }
  .card-top {
    height: 292px;
    padding: 62px 0 0 58px;
    background: linear-gradient(160deg, var(--card-black) 0%, var(--card-black) 45%, var(--card-black-soft) 100%);
    position: relative;
  }
  .company-name {
    font-family: "Roboto Condensed", "Arial Narrow", sans-serif;
    font-weight: 700;
    font-size: 54px;
    letter-spacing: 0.2px;
    color: var(--text-white);
    line-height: 1.1;
  }
  .tagline {
    margin-top: 8px;
    font-weight: 300;
    font-size: 22px;
    color: var(--text-light);
    letter-spacing: 0.3px;
  }
  .website {
    position: absolute;
    left: 58px;
    bottom: 16px;
    font-size: 16px;
    color: var(--text-light);
  }
  .card-band {
    height: 188px;
    background: var(--band-grey);
    padding: 26px 58px 0;
    color: var(--text-band);
    font-size: 16px;
    line-height: 1.5;
  }
  .card-band strong { font-weight: 700; color: var(--text-white); }
</style>
</head>
<body>
  <main class="canvas">
    <article class="business-card">
      <section class="card-top">
        <h1 class="company-name">Brackwell Holdings</h1>
        <p class="tagline">Construction Management in the Palm Beaches</p>
        <p class="website">www.BrackwellHoldings.example</p>
      </section>
      <section class="card-band">
        <p class="contact-line"><strong>Brackwell Holdings</strong>, LLC Construction Management Dean T Brackwell</p>
        <p class="contact-line">418 Ostrander Court #73 North Palm Beach, FL 33412</p>
        <p class="contact-line"><strong>(561) 555-0187</strong></p>
        <p class="contact-line">Contractor License <strong>CGC 7390462</strong></p>
      </section>
    </article>
  </main>
</body>
</html>
```